Residential and Comercial Roofing and Siding Business card design

We need a business card design for a Roofing and Siding company. We have the logo design that have to be in the business card front. We want something professional and clean, black background, maybe with texture, the letters have to be with the colors, green, blue and white.

Industry/Entity Type

Roofing

Contact Information for Business Card

Everything that I want I send in a picture. That is just a idea so you can know what I need but you can be creative.

Font styles to use
Serif
Sans Serif
Script

Colors
0592cd
abd036

Requirements
Must have
• The card have to be vertical.
Should not have
• Any work pictures

```html
<!DOCTYPE html>
<html lang="en">
<head>
<meta charset="utf-8">
<title>Halden Home Improvement LLC – Business Card</title>
<link rel="stylesheet" href="https://fonts.googleapis.com/css2?family=Oswald:wght@300;400&display=swap">
<style>
  :root {
    --card-top: #131313;
    --card-panel: #2a2a2a;
    --card-panel-edge: #232323;
    --card-bottom: #1a1a1a;
    --ink: #ffffff;
    --brand-blue: #0592cd;
    --brand-green: #abd036;
    --brand-grey: #cfcfcf;
  }
  * { margin: 0; padding: 0; box-sizing: border-box; }
  html, body {
    width: 686px;
    height: 1200px;
    overflow: hidden;
    background: var(--card-top);
  }
  .card {
    position: relative;
    width: 686px;
    height: 1200px;
    background: var(--card-top);
    font-family: "Oswald", "Arial Narrow", sans-serif;
    color: var(--ink);
  }
  .brand {
    position: absolute;
    top: 146px;
    left: 0;
    width: 100%;
    display: flex;
    justify-content: center;
    align-items: center;
    gap: 20px;
  }
  .brand-square {
    width: 124px;
    height: 124px;
    background: var(--brand-grey);
  }
  .brand-name {
    font-weight: 400;
    color: var(--brand-blue);
    text-transform: uppercase;
    line-height: 1.05;
  }
  .brand-name .primary {
    display: block;
    font-size: 62px;
    letter-spacing: 3px;
  }
  .brand-name .secondary {
    display: block;
    font-size: 25px;
    letter-spacing: 1px;
  }
  .brand-name .tagline {
    display: block;
    margin-top: 4px;
    font-size: 15px;
    letter-spacing: 3px;
    text-align: center;
  }
  .services-panel {
    position: absolute;
    top: 366px;
    left: 0;
    width: 100%;
    height: 724px;
    background: linear-gradient(90deg, var(--card-panel-edge) 0%, var(--card-panel) 50%, var(--card-panel-edge) 100%);
  }
  .service-list {
    list-style: none;
    text-align: center;
    padding-top: 22px;
  }
  .service {
    font-weight: 400;
    font-size: 48px;
    letter-spacing: 3.5px;
    line-height: 57px;
    text-transform: uppercase;
    margin-bottom: 57px;
  }
  .service .amp { color: var(--brand-green); }
  .service.credentials {
    margin-bottom: 0;
    color: var(--brand-green);
  }
  .service.credentials .licensed { color: var(--brand-blue); }
  .card-foot {
    position: absolute;
    left: 0;
    bottom: 0;
    width: 100%;
    height: 110px;
    background: var(--card-bottom);
  }
</style>
</head>
<body>
  <main class="card">
    <header class="brand">
      <span class="brand-square" aria-hidden="true"></span>
      <h1 class="brand-name">
        <span class="primary">Halden</span>
        <span class="secondary">Home Improvement LLC</span>
        <span class="tagline">Roofing &amp; Siding</span>
      </h1>
    </header>

    <section class="services-panel">
      <ul class="service-list">
        <li class="service">Residental <span class="amp">&amp;</span> Comercial</li>
        <li class="service">Roofing <span class="amp">&amp;</span> Siding</li>
        <li class="service">Window <span class="amp">&amp;</span> Doors</li>
        <li class="service">Skylights</li>
        <li class="service">Gutters <span class="amp">&amp;</span> Leader</li>
        <li class="service credentials">Free Estimate<br><span class="licensed">Licensed &amp; Insured</span></li>
      </ul>
    </section>

    <footer class="card-foot"></footer>
  </main>
</body>
</html>
```